DM - management consultant

Business card - contemporary design

Front info
Dorian Maples

(Address not necessary)
PO Box 7386
Belmont, CA 94002

(650) 555-0143
dm@dorianmapl.es

Twitter: dmq527
Facebook: /Dorian.Maples
Linkedin: /in/dorianmaples

Back or Front
www.dorianmaples.net
Facilitation & coaching, change management, strategic partnerships, business improvement

Target Market(s)

High tech businesses - mostly startups in Silicon Valley

Industry/Entity Type

Business

Font styles to use
Sans Serif

Colors

Designer to choose colors to be used in the design.

```html
<!DOCTYPE html>
<html lang="en">
<head>
<meta charset="utf-8">
<title>Dorian Maples – Business Card Back</title>
<link rel="stylesheet" href="https://fonts.googleapis.com/css2?family=Antonio:wght@300;400&display=swap">
<style>
  :root {
    --card-bg: #000000;
    --ink: #ffffff;
    --ink-soft: #bfbfbf;
  }
  html, body {
    margin: 0;
    padding: 0;
    width: 694px;
    height: 1200px;
    overflow: hidden;
    background: var(--card-bg);
  }
  .card-back {
    position: relative;
    width: 694px;
    height: 1200px;
    background: var(--card-bg);
  }
  .card-back__art {
    position: absolute;
    left: 0;
    top: 0;
    width: 694px;
    height: 1200px;
  }
  .web-address {
    fill: var(--ink);
    font-family: "Antonio", "Oswald", sans-serif;
    font-weight: 400;
    font-size: 66px;
    font-variant: small-caps;
  }
  .services {
    fill: var(--ink-soft);
    font-family: "Antonio", "Oswald", sans-serif;
    font-weight: 300;
    font-size: 24px;
    letter-spacing: 2px;
    text-transform: uppercase;
  }
</style>
</head>
<body>
  <main class="card-back">
    <svg class="card-back__art" width="694" height="1200" viewBox="0 0 694 1200">
      <text class="web-address" x="37" y="626" textLength="622" lengthAdjust="spacingAndGlyphs">www.DorianMaples.net</text>
      <text class="services" x="347" y="690" text-anchor="middle">Facilitation &amp; Coaching · Change Management</text>
      <text class="services" x="347" y="726" text-anchor="middle">Strategic Partnerships · Business Improvement</text>
    </svg>
  </main>
</body>
</html>
```